July 4th Postcard to existing clients

5x7 postcard wishing our clients happy 4th of July. Card should read on the back "Thank You For Being A Valued Client!. Stay Safe And Enjoy Your Independence Day Celebrations!"

Patriotic theme with fireworks is ideal. We are a law firm so should still have a feel of professionalism while still being fun since it is for a fun holiday.

```html
<!DOCTYPE html>
<html lang="en">
<head>
<meta charset="utf-8">
<title>Happy 4th of July Postcard – Hartwell Law Firm</title>
<link rel="stylesheet" href="https://fonts.googleapis.com/css2?family=Marcellus&family=Great+Vibes&family=Open+Sans:wght@400;700&display=swap">
<style>
  :root {
    --stage: #dcdcdc;
    --ink: #000000;
    --paper: #ffffff;
    --navy: #1c2f5c;
    --deep-navy: #0d1730;
    --flag-red: #9e1f24;
    --ember: #d9542a;
    --sunset: #f2a347;
    --slate: #5f6472;
    --script-ink: #111111;
  }
  * { box-sizing: border-box; margin: 0; padding: 0; }
  html, body {
    width: 1200px;
    height: 1200px;
    overflow: hidden;
    background: var(--stage);
  }
  .postcard {
    position: absolute;
    left: 220px;
    width: 762px;
    height: 547px;
    overflow: hidden;
  }
  .postcard--front { top: 37px; background: var(--ink); }
  .postcard--back { top: 601px; display: flex; background: var(--paper); }

  /* Front */
  .front-photo {
    position: absolute;
    inset: 0 0 118px 0;
    background:
      radial-gradient(ellipse 120px 50px at 22% 96%, var(--sunset) 0%, rgba(242,163,71,0) 100%),
      radial-gradient(ellipse 420px 200px at 70% 40%, rgba(158,31,36,0.9) 0%, rgba(158,31,36,0) 100%),
      radial-gradient(ellipse 320px 120px at 20% 82%, rgba(217,84,42,0.85) 0%, rgba(217,84,42,0) 100%),
      linear-gradient(160deg, var(--navy) 0%, #2d4a86 28%, #6a3a4c 55%, var(--flag-red) 80%, #2a1a20 100%);
  }
  .front-title {
    position: absolute;
    left: 0;
    right: 0;
    bottom: 40px;
    text-align: center;
    color: var(--paper);
    font-family: "Marcellus", serif;
    font-weight: 400;
    font-size: 66px;
    letter-spacing: 2px;
    line-height: 1;
    white-space: nowrap;
  }
  .front-title .day-number {
    display: inline-block;
    font-size: 124px;
    position: relative;
    top: 14px;
    margin-left: 14px;
  }
  .front-title .day-suffix {
    display: inline-block;
    font-family: "Great Vibes", cursive;
    font-size: 68px;
    letter-spacing: 0;
    margin: 0 22px 0 -18px;
    position: relative;
    top: -16px;
  }

  /* Back */
  .back-art {
    position: relative;
    width: 378px;
    height: 100%;
    overflow: hidden;
    background: var(--ink);
  }
  .back-photo {
    position: absolute;
    inset: 0;
    background:
      radial-gradient(ellipse 160px 90px at 20% 32%, rgba(217,84,42,0.85) 0%, rgba(217,84,42,0) 100%),
      linear-gradient(175deg, var(--deep-navy) 0%, #2b2f55 14%, var(--flag-red) 30%, #3a1c26 55%, #120c12 100%);
  }
  .return-address {
    position: absolute;
    left: 47px;
    top: 26px;
    color: var(--paper);
    font-family: "Open Sans", sans-serif;
    font-style: normal;
    font-weight: 700;
    font-size: 16px;
    line-height: 1.22;
  }
  .greeting-panel {
    position: absolute;
    left: 4px;
    top: 168px;
    width: 360px;
    height: 420px;
    transform: rotate(-2deg);
    background: radial-gradient(ellipse 230px 250px at 50% 40%, var(--paper) 0%, #f3f3f3 45%, #9a9a9a 75%, #1a1a1a 100%);
    text-align: center;
  }
  .greeting-thanks {
    margin-top: 30px;
    font-family: "Great Vibes", cursive;
    font-size: 28px;
    line-height: 1.2;
    color: var(--script-ink);
  }
  .greeting-message {
    margin-top: 6px;
    font-family: "Great Vibes", cursive;
    font-size: 38px;
    line-height: 46px;
    color: var(--script-ink);
  }
  .firm-name {
    margin-top: 44px;
    font-family: "Open Sans", sans-serif;
    font-weight: 400;
    font-size: 23px;
    letter-spacing: 1px;
    color: var(--slate);
  }
  .address-side {
    flex: 1;
    background: var(--paper);
  }
</style>
</head>
<body>
  <section class="postcard postcard--front">
    <div class="front-photo" role="img" aria-label="Statue of Liberty silhouetted against a waving American flag, fireworks and a sunset sky"></div>
    <h1 class="front-title">HAPPY<span class="day-number">4</span><span class="day-suffix">th</span>OF JULY</h1>
  </section>

  <section class="postcard postcard--back">
    <div class="back-art">
      <div class="back-photo" role="img" aria-label="American flag and red fireworks over a dark night sky"></div>
      <address class="return-address">
        HARTWELL LAW FIRM<br>
        1480 N Maple Crest Ave<br>
        Fairview, MO 65999
      </address>
      <div class="greeting-panel">
        <p class="greeting-thanks">Thank You For Being A Valued Client!</p>
        <p class="greeting-message">Stay Safe and Enjoy<br>Your Independence<br>Day Celebrations!</p>
        <p class="firm-name">HARTWELL LAW</p>
      </div>
    </div>
    <div class="address-side"></div>
  </section>
</body>
</html>
```